DEAN COLLOPY PROPERTY SERVICES

I want a business card that is clean and simple.
'Dean Collopy Property Services' is the title.
Somewhere on the card needs to be 'Carpentry, Tiling, painting and garden services'

On the back of card
PH 087 394 1526
email: deancollopypropertyservices@fernmail.net

I have attached a picture of my other business. I would like the font and design to be similar to the bathroom business.

Many thanks.

```html
<!DOCTYPE html>
<html lang="en">
<head>
<meta charset="utf-8">
<title>Dean Collopy Property Services — Business Card</title>
<link rel="stylesheet" href="https://fonts.googleapis.com/css2?family=Montserrat:wght@400;500;600&display=swap">
<style>
  :root {
    --backdrop: #7a5e3e;
    --card: #050707;
    --ink: #f2f2f2;
    --tab: #d4d4d4;
    --font: "Montserrat", sans-serif;
  }
  * { margin: 0; padding: 0; box-sizing: border-box; }
  html, body {
    width: 900px;
    height: 1200px;
    overflow: hidden;
  }
  body {
    position: relative;
    background: var(--backdrop);
    font-family: var(--font);
    color: var(--ink);
  }
  .card {
    position: absolute;
    width: 773px;
    height: 448px;
    background: var(--card);
  }
  .card--front { left: 72px; top: 135px; }
  .card--back  { left: 74px; top: 625px; }

  /* Front */
  .services {
    position: absolute;
    top: 50px;
    width: 350px;
    height: 24px;
    font-size: 18px;
    font-weight: 400;
    letter-spacing: 3.4px;
    line-height: 24px;
    text-align: center;
    white-space: nowrap;
    transform-origin: center;
  }
  .services--left {
    left: -130px;
    top: 163px;
    transform: rotate(-90deg);
  }
  .services--right {
    left: 556px;
    top: 163px;
    transform: rotate(-90deg);
  }
  .services .divider { margin: 0 12px; }

  .brand {
    position: absolute;
    left: 0;
    right: 0;
    top: 160px;
    text-align: center;
  }
  .brand__name {
    font-size: 63px;
    font-weight: 500;
    line-height: 1;
    letter-spacing: 0.5px;
  }
  .brand__tagline {
    margin-top: 14px;
    font-size: 23px;
    font-weight: 500;
    letter-spacing: 4.2px;
    line-height: 1;
  }

  /* Back */
  .tab {
    position: absolute;
    top: 178px;
    width: 19px;
    height: 94px;
    background: var(--tab);
  }
  .tab--left { left: 0; }
  .tab--right { right: 0; }

  .contact {
    position: absolute;
    left: 0;
    right: 0;
    top: 193px;
    text-align: center;
    font-weight: 500;
  }
  .contact__phone {
    font-size: 18px;
    letter-spacing: 3px;
    line-height: 22px;
  }
  .contact__email {
    margin-top: 21px;
    font-size: 17px;
    letter-spacing: 2px;
    line-height: 22px;
  }
</style>
</head>
<body>
  <section class="card card--front" aria-label="Card front">
    <p class="services services--left">CARPENTRY<span class="divider">|</span>PAINTING</p>
    <div class="brand">
      <h1 class="brand__name">Dean Collopy</h1>
      <p class="brand__tagline">PROPERTY SERVICES</p>
    </div>
    <p class="services services--right">TILING<span class="divider">|</span>GARDEN SERVICES</p>
  </section>

  <section class="card card--back" aria-label="Card back">
    <span class="tab tab--left"></span>
    <div class="contact">
      <p class="contact__phone">PH 087 394 1526</p>
      <p class="contact__email">DEANCOLLOPYPROPERTYSERVICES@FERNMAIL.NET</p>
    </div>
    <span class="tab tab--right"></span>
  </section>
</body>
</html>
```